Business card design needed

We need a new business card design to re launch my carpentry business. Could include double sided card with list of services provided.
Kitchens, bathrooms, decks, pergolas, window replacements, timber floor installation, owner builder assistance and general carpentry.
Would like an eye catching card that becons to be read in bright colors that has a logo that could be also used on clothing vehicle sinage etc
Preferably in blues and reds we live near beach so maybe some type of Beecher feel
Target Market(s)
The target market of my business would be mainly individuals requiring professional carpentry services not just a handy man. The renovation market plays a big part of my business
Industry/Entity Type
Carpentry
Contact Information for Business Card
Carpenter & joiner
Mel Hartigan
Wrenhaven
lorika_mel@quellpost.com
0493816025
Look and feel

```html
<!DOCTYPE html>
<html lang="en">
<head>
<meta charset="utf-8">
<title>Mel Hartigan – Carpenter &amp; Joiner</title>
<link rel="stylesheet" href="https://fonts.googleapis.com/css2?family=Philosopher:ital,wght@0,400;0,700;1,700&display=swap">
<style>
  :root {
    --card-black: #000000;
    --amber: #dc911b;
    --white: #ffffff;
  }
  html, body {
    margin: 0;
    padding: 0;
    width: 1200px;
    height: 693px;
    overflow: hidden;
    background: var(--card-black);
  }
  .card {
    position: relative;
    width: 1200px;
    height: 693px;
    background: var(--card-black);
    font-family: "Philosopher", sans-serif;
  }
  .brand {
    position: absolute;
    left: 120px;
    top: 322px;
    display: flex;
    align-items: center;
    gap: 14px;
  }
  .brand-dot {
    width: 24px;
    height: 24px;
    border-radius: 50%;
    background: var(--amber);
    flex: none;
  }
  .brand-name {
    color: var(--amber);
    font-weight: 700;
    font-size: 34px;
    line-height: 1;
    white-space: nowrap;
  }
  .details {
    position: absolute;
    right: 116px;
    top: 0;
    text-align: right;
  }
  .value {
    position: absolute;
    right: 0;
    white-space: nowrap;
    color: var(--white);
    font-weight: 400;
    font-size: 38px;
    line-height: 1;
  }
  .label {
    position: absolute;
    right: 0;
    white-space: nowrap;
    color: var(--amber);
    font-weight: 700;
    font-style: italic;
    font-size: 31px;
    line-height: 1;
  }
  .owner-name { top: 192px; }
  .trade { top: 236px; }
  .email { top: 342px; }
  .email-label { top: 385px; right: 6px; }
  .phone { top: 469px; }
  .phone-label { top: 515px; }
</style>
</head>
<body>
  <main class="card">
    <div class="brand">
      <span class="brand-dot"></span>
      <span class="brand-name">Hartigan Timberworks</span>
    </div>
    <div class="details">
      <div class="value owner-name">Mel Hartigan Wrenhaven</div>
      <div class="label trade">Carpenter &amp; Joiner</div>
      <div class="value email">lorika_mel@quellpost.com</div>
      <div class="label email-label">e-mail</div>
      <div class="value phone">0493816025</div>
      <div class="label phone-label">Telephone</div>
    </div>
  </main>
</body>
</html>
```